Business Card Design

Lawyer
Business name "HarlowLaw"
Areas of expertise:
property
commercial
trusts
immigration
franchising
I want the following quote on the back of the card somewhere.
"Education is when you read the fine print,
experience is what you get if you don't." Miles Corbell
Probably the "areas of expertise" should be on the back also to avoid cluttering the front.
As for colours, I like the shades of blue used on qerivo.com.
The basic part of the card with the contact info needs to be white and uncluttered.
Target Market(s)
small to medium sized self employed business people
Industry/Entity Type
Business
Contact Information for Business Card
Dennis Harlow
Phone + 64 9 517 4460
Fax: + 64 9 517 4461
PO Box 742
Clevedon
Auckland 2248
NZ
email: dennis@pinecrestlegal.co.nz

```html
<!DOCTYPE html>
<html lang="en">
<head>
<meta charset="utf-8">
<title>Harlow Law – Business Card</title>
<link rel="stylesheet" href="https://fonts.googleapis.com/css2?family=Cinzel:wght@400;600&family=Lato:wght@400;700&display=swap">
<style>
  :root {
    --bg: #2b2b2b;
    --card-white: #ffffff;
    --card-shade: #e9ecef;
    --brand-blue: #1f72b1;
    --brand-blue-dark: #17609a;
    --navy: #14355c;
    --slate: #4f6f8c;
    --contact-blue: #2a73b3;
    --icon: #3c4a57;
    --band-text: #e6eef6;
  }
  * { box-sizing: border-box; margin: 0; padding: 0; }
  html, body { width: 1200px; height: 997px; overflow: hidden; }
  body {
    background: var(--bg);
    display: flex;
    flex-direction: column;
    align-items: center;
    justify-content: center;
    gap: 60px;
  }
  .card {
    position: relative;
    width: 700px;
    height: 400px;
    border-radius: 22px;
    overflow: hidden;
    background: radial-gradient(ellipse at 40% 35%, var(--card-white) 45%, var(--card-shade) 100%);
    box-shadow: 0 14px 30px rgba(0,0,0,0.45);
  }

  /* Back */
  .back-title {
    position: absolute;
    top: 120px; left: 0; right: 0;
    text-align: center;
    font-family: "Cinzel", serif;
    font-weight: 600;
    font-size: 58px;
    letter-spacing: 2px;
    color: var(--slate);
  }
  .back-rule {
    position: absolute;
    left: 0; right: 0;
    top: 282px;
    height: 8px;
    background: var(--brand-blue);
  }
  .back-band {
    position: absolute;
    left: 0; right: 0; bottom: 0;
    top: 298px;
    background: linear-gradient(var(--brand-blue), var(--brand-blue-dark));
    display: flex;
    flex-direction: column;
    justify-content: center;
    align-items: center;
    gap: 4px;
  }
  .quote-line {
    font-family: "Cinzel", serif;
    font-size: 18px;
    letter-spacing: 1px;
    color: var(--band-text);
  }

  /* Front */
  .holder {
    position: absolute;
    top: 28px; left: 0;
    display: flex;
    align-items: center;
    gap: 10px;
    font-family: "Cinzel", serif;
    font-size: 19px;
    letter-spacing: 1px;
    color: var(--brand-blue);
  }
  .holder-mark { width: 8px; height: 24px; background: var(--brand-blue); }
  .front-title {
    position: absolute;
    top: 116px; left: 48px;
    font-family: "Cinzel", serif;
    font-weight: 600;
    font-size: 46px;
    letter-spacing: 2px;
    color: var(--navy);
  }
  .contact-list {
    position: absolute;
    left: 34px; bottom: 40px;
    list-style: none;
    font-family: "Lato", sans-serif;
    font-size: 19px;
    color: var(--contact-blue);
  }
  .contact-list li { display: flex; align-items: center; gap: 14px; height: 32px; white-space: nowrap; }
  .contact-list svg { width: 16px; height: 16px; fill: var(--icon); flex: none; }
  .divider {
    position: absolute;
    top: 0; bottom: 0;
    left: 436px;
    width: 8px;
    background: var(--brand-blue);
  }
  .expertise {
    position: absolute;
    top: 0; bottom: 0; right: 0;
    left: 456px;
    background: linear-gradient(var(--brand-blue), var(--brand-blue-dark));
    padding: 44px 0 0 22px;
    font-family: "Cinzel", serif;
    color: #eef4fa;
  }
  .expertise h2 {
    font-weight: 400;
    font-size: 17px;
    letter-spacing: 1px;
    margin-bottom: 40px;
    white-space: nowrap;
  }
  .expertise ul { list-style: disc; padding-left: 36px; font-size: 20px; letter-spacing: 1px; }
  .expertise li { line-height: 37px; white-space: nowrap; }
</style>
</head>
<body>
  <section class="card card-back" aria-label="Card back">
    <h1 class="back-title">Harlow Law</h1>
    <div class="back-rule"></div>
    <div class="back-band">
      <p class="quote-line">EDUCATION IS WHEN YOU READ THE FINE PRINT</p>
      <p class="quote-line">EXPERIENCE IS WHAT YOU GET IF YOU DON'T- MILES CORBELL</p>
    </div>
  </section>

  <section class="card card-front" aria-label="Card front">
    <p class="holder"><span class="holder-mark"></span>DENNIS HARLOW</p>
    <h1 class="front-title">Harlow Law</h1>
    <ul class="contact-list">
      <li><svg viewBox="0 0 16 16" aria-hidden="true"><path d="M4 0h8a1 1 0 0 1 1 1v14a1 1 0 0 1-1 1H4a1 1 0 0 1-1-1V1a1 1 0 0 1 1-1zm1 2v10h6V2zm3 11a1 1 0 1 0 0 2 1 1 0 0 0 0-2z"/></svg>+ 64 9 517 4460</li>
      <li><svg viewBox="0 0 16 16" aria-hidden="true"><path d="M4 1h7v4H4zM1 6h14v8H1zm2 2v2h4V8zm8 0v1h2V8zm0 2v1h2v-1z"/></svg>+ 64 9 517 4461</li>
      <li><svg viewBox="0 0 16 16" aria-hidden="true"><path d="M0 3h16v10H0zm1.5 1L8 9l6.5-5z"/></svg>dennis@pinecrestlegal.co.nz</li>
      <li><svg viewBox="0 0 16 16" aria-hidden="true"><path d="M8 0a8 8 0 1 0 0 16A8 8 0 0 0 8 0zm0 2a6 6 0 0 1 6 6H9V2.1zM7 2.1V8H2a6 6 0 0 1 5-5.9z"/></svg>PO Box 742 Tarvin Heights 2315 NZ</li>
    </ul>
    <div class="divider"></div>
    <div class="expertise">
      <h2>AREAS OF EXPERTISE:</h2>
      <ul>
        <li>TRUSTS</li>
        <li>PROPERTY</li>
        <li>COMMERCIAL</li>
        <li>IMMIGRATION</li>
        <li>FRANCHISING</li>
      </ul>
    </div>
  </section>
</body>
</html>
```